Residential Construction Business - Site Signage

I need a design made for a site fence banner. We have a logo and branding so the design would need to be aligned with this. It would need to be made to specific size ratio so that it can be sent to the maker for production.
ratio : 4600 wide x 1700 high
The design should feature our website and also the slogan
"don't move, re-imagine"

Target Market(s)

potential clients

Industry/Entity Type

construction

Font styles to use
Other font styles liked:
• to match branding

Colors
0054AA
0677BA
7BADD7
CADEEF
E8F1F8

Requirements
Must have
• www.velmbuild.com.au Majority of the sign is our brand logo
Nice to have
• Majority of the sign is our brand logo
Should not have
• colors and themes that arent brand relevant

```html
<!DOCTYPE html>
<html lang="en">
<head>
<meta charset="utf-8">
<title>Velm Build – Site Fence Banner</title>
<link href="https://fonts.googleapis.com/css2?family=Montserrat:wght@600;700&display=swap" rel="stylesheet">
<style>
  :root {
    --backdrop: #d4d4d4;
    --navy: #0f3659;
    --charcoal: #2c3432;
    --paper: #f5f5f5;
    --pattern-light: #f3f3f3;
    --pattern-mid: #e2e2e2;
    --white: #ffffff;
  }
  html, body {
    margin: 0;
    width: 1200px;
    height: 1200px;
    overflow: hidden;
    background: var(--backdrop);
  }
  .banner {
    position: absolute;
    left: 52px;
    top: 411px;
    width: 1090px;
    height: 391px;
    background: var(--paper);
    box-shadow: 0 4px 8px rgba(0,0,0,0.18);
    overflow: hidden;
    font-family: "Montserrat", sans-serif;
  }
  .geometric-backdrop {
    position: absolute;
    left: 497px;
    top: 0;
    width: 593px;
    height: 391px;
    background: linear-gradient(135deg, var(--paper) 0%, var(--pattern-light) 35%, var(--pattern-mid) 60%, var(--pattern-light) 80%, var(--paper) 100%);
  }
  .brand-panel {
    position: absolute;
    left: 0;
    top: 0;
    width: 440px;
    height: 391px;
  }
  .brand-name {
    position: absolute;
    left: 0;
    width: 250px;
    top: 192px;
    transform: translateY(-50%);
    text-align: center;
    color: var(--white);
    font-weight: 700;
    font-size: 22px;
    letter-spacing: 6px;
    white-space: nowrap;
  }
  .slogan {
    position: absolute;
    left: 607px;
    top: 139px;
    height: 105px;
    border-left: 5px solid var(--navy);
    padding-left: 13px;
  }
  .slogan-line {
    display: block;
    font-weight: 700;
    font-size: 56px;
    line-height: 64px;
    letter-spacing: 0.5px;
    white-space: nowrap;
  }
  .slogan-line--first { color: var(--navy); margin-top: -10px; }
  .slogan-line--second { color: var(--charcoal); }
  .website {
    position: absolute;
    left: 606px;
    top: 317px;
    color: var(--navy);
    font-weight: 600;
    font-size: 20px;
    letter-spacing: 1.3px;
    white-space: nowrap;
  }
</style>
</head>
<body>
  <div class="banner">
    <div class="geometric-backdrop" role="img" aria-label="Soft grey architectural line pattern of overlapping squares and diagonals"></div>
    <svg class="brand-panel" viewBox="0 0 440 391" aria-hidden="true">
      <path d="M0 0 H381 L254 176 Q244 196 254 212 L387 391 H0 Z" fill="var(--navy)"/>
    </svg>
    <div class="brand-name">VELM BUILD</div>
    <div class="slogan">
      <span class="slogan-line slogan-line--first">DON’T MOVE,</span>
      <span class="slogan-line slogan-line--second">RE-IMAGINE</span>
    </div>
    <div class="website">WWW.VELMBUILD.COM.AU</div>
  </div>
</body>
</html>
```